House flipping business web site needed

pinecrestholdingsgroup.com.
I am a residential developer in Northern NJ and I am looking for a fresh new updated website. I have an intro video about my company being made now. I don't update it very often but I want an easy format that I can add update photos to on projects I have worked on or homes I renovate for sale.

Target Market(s)

investors into my projects so a portfolio , people looking to sell their homes to me.

Industry/Entity Type

Real Estate Development

Number of Pages Required

4 page

Font styles to use
Serif

Colors
33b8a4
39a9d7
cadf82

Requirements
Must have
• space for an intro video about my company
• a portfolio with pictures and information about each project
• Markets we serve- Morris County, NJ
• My logo- already created
• SEO
• Yes I would like this to function over all platforms. Phone, computer, all platforms.
• history and background page
• I am looking for a completed page that I can upload to the site that hosts my website
Nice to have
• I want something creative, easy to navigate. modern.

```html
<!DOCTYPE html>
<html lang="en">
<head>
<meta charset="utf-8">
<title>Pinecrest Holdings Group</title>
<link rel="stylesheet" href="https://fonts.googleapis.com/css2?family=Raleway:wght@300;400;500&family=Open+Sans:wght@400;600;700&family=Parisienne&display=swap">
<style>
:root{
  --blue:#2fa0d8;
  --blue-deep:#2b7ec1;
  --text:#333;
  --muted:#5e5e5e;
  --footer:#545456;
  --frame:#cfcfcf;
  --white:#fff;
}
*{margin:0;padding:0;box-sizing:border-box}
html,body{width:1200px;height:2679px;overflow:hidden;background:var(--white)}
body{position:relative;font-family:"Open Sans",Arial,sans-serif;color:var(--text)}
h1,h2,h3,h4,h5{font-weight:400}
.abs{position:absolute}
.topbar{left:0;top:0;width:1200px;height:40px;background:var(--blue);color:var(--white);display:flex;justify-content:flex-end;align-items:center;gap:34px;padding-right:78px;font-size:15px}
.topbar span{display:flex;align-items:center;gap:10px}
.topbar .phone{font-weight:700;font-size:21px}
.brand{left:70px;top:46px;width:220px;display:flex;flex-direction:column;align-items:center;gap:6px;z-index:2}
.brand .dot{width:42px;height:42px;border-radius:50%;background:var(--blue)}
.brand .name{font-family:"Raleway",sans-serif;font-weight:500;color:var(--blue-deep);font-size:17px;line-height:19px;text-align:center;letter-spacing:1px;white-space:nowrap}
.nav{top:92px;right:77px;display:flex;gap:56px;font-family:"Raleway",sans-serif;font-size:24px;color:#444;z-index:2}
.nav .current{color:var(--blue)}
.hero{left:0;top:150px;width:1200px;height:511px;background:linear-gradient(180deg,#5d7a3a 0%,#7a7a66 35%,#a9a89a 55%,#5f8a34 85%,#4e7a2a 100%)}
.header-wave{left:0;top:100px;width:1200px;height:100px}
.tagline{left:0;top:661px;width:1200px;height:125px;background:linear-gradient(90deg,#2d88b2,#4aaed2 50%,#2d88b2);display:flex;align-items:center;justify-content:center}
.tagline p{font-family:"Parisienne",cursive;color:var(--white);font-size:40px}
.welcome-kicker{left:77px;top:838px;font-family:"Raleway",sans-serif;font-weight:300;font-size:27px;color:#555}
.welcome-title{left:77px;top:880px;width:540px;font-family:"Raleway",sans-serif;font-size:34px;color:var(--blue-deep);white-space:nowrap}
.welcome-copy{left:77px;top:944px;width:525px;font-size:15px;line-height:25px;color:var(--muted)}
.btn{left:77px;top:1143px;width:166px;height:50px;background:var(--blue-deep);color:var(--white);font-family:"Raleway",sans-serif;font-size:20px;display:flex;align-items:center;justify-content:center;border-radius:3px}
.video{left:643px;top:848px;width:480px;height:344px;border:11px solid var(--frame);background:linear-gradient(180deg,#4d5358,#3c4044 55%,#2f3433)}
.video .play{position:absolute;left:50%;top:50%;width:60px;height:60px;margin:-30px 0 0 -30px;border-radius:50%;background:rgba(255,255,255,.85)}
.markets{left:0;top:1254px;width:1200px;height:332px;background:linear-gradient(135deg,#3f8fbf,#2f86b6 50%,#4a9cc8)}
.markets-title{left:0;top:1304px;width:1200px;text-align:center;font-family:"Raleway",sans-serif;font-size:40px;color:var(--white)}
.market-img{width:210px;height:144px;border:4px solid var(--white);top:1371px}
.market-text{top:1366px;width:275px;color:var(--white)}
.market-text h3{font-family:"Raleway",sans-serif;font-size:23px;margin-bottom:6px}
.market-text p{font-size:14.5px;line-height:25px}
.market-text .more{font-size:14px;margin-top:8px;display:flex;align-items:center;gap:6px}
.portfolio-title{left:0;top:1640px;width:1200px;text-align:center;font-family:"Raleway",sans-serif;font-size:40px;color:#555}
.portfolio-title b{font-weight:400;color:var(--blue)}
.project{width:234px;text-align:center}
.project .photo{width:234px;height:156px}
.project h4{font-family:"Raleway",sans-serif;font-size:23px;color:#222;margin-top:14px}
.project p{font-size:13.5px;line-height:23px;color:var(--muted);margin-top:5px}
.footer-wave{left:0;top:2300px;width:1200px;height:60px}
.footer{left:0;top:2345px;width:1200px;height:280px;background:var(--footer)}
.footer-brand{left:85px;top:2425px;width:220px;display:flex;flex-direction:column;align-items:center;gap:10px}
.footer-brand .dot{width:62px;height:62px;border-radius:50%;background:var(--blue)}
.footer-brand .name{font-family:"Raleway",sans-serif;font-weight:500;color:var(--white);font-size:19px;line-height:22px;text-align:center;letter-spacing:1px;white-space:nowrap}
.fcol{top:2400px;color:var(--white)}
.fcol h5{font-family:"Raleway",sans-serif;font-size:22px;margin-bottom:14px}
.links li{list-style:none;font-size:16px;line-height:36px;color:#d4d4d4}
.links li.current{color:var(--white)}
.contact li{list-style:none;display:flex;gap:12px;font-size:14.5px;line-height:22px;margin-bottom:16px}
.contact svg{flex:none;margin-top:3px}
.news p{font-size:14.5px;line-height:22px;width:240px}
.news .field{width:233px;height:36px;background:var(--white);color:#666;font-size:14px;padding:8px;margin-top:6px}
.news .subscribe{width:160px;height:42px;background:var(--blue);color:var(--white);font-family:"Raleway",sans-serif;font-size:21px;display:flex;align-items:center;justify-content:center;margin-top:10px}
.bottombar{left:0;top:2625px;width:1200px;height:54px;background:var(--blue);color:var(--white);font-size:15px;display:flex;align-items:center;justify-content:center}
</style>
</head>
<body>

<header>
  <div class="abs topbar">
    <span><svg width="20" height="15" viewBox="0 0 20 15"><rect x="1" y="1" width="18" height="13" fill="none" stroke="#fff" stroke-width="1.8"/><path d="M1 1 L10 8 L19 1" fill="none" stroke="#fff" stroke-width="1.8"/></svg>info@pinecrestholdingsgroup.com</span>
    <span class="phone"><svg width="20" height="20" viewBox="0 0 24 24"><path fill="#fff" d="M6.6 10.8a15 15 0 0 0 6.6 6.6l2.2-2.2c.3-.3.7-.4 1-.2 1.1.4 2.3.6 3.6.6.6 0 1 .4 1 1V20c0 .6-.4 1-1 1A17 17 0 0 1 3 4c0-.6.4-1 1-1h3.5c.6 0 1 .4 1 1 0 1.3.2 2.5.6 3.6.1.3 0 .7-.2 1z"/></svg>123 456 7890</span>
  </div>
  <div class="abs hero" role="img" aria-label="Photo of a small weathered cottage among trees before renovation"></div>
  <svg class="abs header-wave" viewBox="0 0 1200 100" preserveAspectRatio="none">
    <path d="M0 0 H1200 V50 C950 40 760 62 560 70 C350 78 150 75 0 55 Z" fill="#fff"/>
    <path d="M0 55 C150 75 350 78 560 70 C760 62 950 40 1200 50" fill="none" stroke="#2fa0d8" stroke-width="7"/>
  </svg>
  <div class="abs brand"><div class="dot"></div><div class="name">PINECREST<br>HOLDINGS GROUP</div></div>
  <nav class="abs nav"><span class="current">HOME</span><span>ABOUT</span><span>PORTFOLIO</span><span>CONTACT</span></nav>
</header>

<section class="abs tagline" role="img" aria-label="Blue lake water backdrop">
  <p>We bring excellence to the home buying and renovation business.</p>
</section>

<section class="welcome">
  <p class="abs welcome-kicker">WELCOME TO</p>
  <h1 class="abs welcome-title">PINECREST HOLDINGS GROUP</h1>
  <p class="abs welcome-copy">We are a team of experienced home buyers and renovators in the Morris County, NJ area. Our specialty is purchasing distressed homes and property. We then collaborate with the best talents in Northern New Jersey to renovate those properties and transform them into the best house in the neighborhood. As a result we create equity, a return on investment and most importantly we give home buyers a worry free property that provides a better way of life and hope for their future.</p>
  <a class="abs btn">READ MORE</a>
  <div class="abs video" role="img" aria-label="Intro video still of a renovated two-storey house"><span class="play"><svg width="60" height="60" viewBox="0 0 60 60"><path d="M24 18 L42 30 L24 42 Z" fill="#444"/></svg></span></div>
</section>

<section>
  <div class="abs markets" role="img" aria-label="Blue-tinted photo of a renovated kitchen interior"></div>
  <h2 class="abs markets-title">MARKETS WE SERVE</h2>
  <div class="abs market-img" style="left:77px;background:linear-gradient(180deg,#8a7f8a,#b3a7a8 55%,#e8e8ee)" role="img" aria-label="Snowy yard in front of a house in Morris County"></div>
  <div class="abs market-text" style="left:298px">
    <h3>Morris Country</h3>
    <p>We only buy and renovate homes in our neighborhoods right here in the Morris County, NJ area. Is a house in your neighborhood an eyesore?</p>
    <p class="more">READ MORE <svg width="12" height="12" viewBox="0 0 12 12"><path d="M1 1l5 5-5 5M6 1l5 5-5 5" fill="none" stroke="#fff" stroke-width="1.6"/></svg></p>
  </div>
  <div class="abs market-img" style="left:618px;background:linear-gradient(180deg,#6fa3d6,#9dc0e0 45%,#b5a98f 65%,#4f7ea6)" role="img" aria-label="City skyline across a river in New Jersey"></div>
  <div class="abs market-text" style="left:840px">
    <h3>New Jersey</h3>
    <p>We only buy and renovate homes in our neighborhoods right here in the Morris County, NJ area. Is a house in your neighborhood an eyesore?</p>
    <p class="more">READ MORE <svg width="12" height="12" viewBox="0 0 12 12"><path d="M1 1l5 5-5 5M6 1l5 5-5 5" fill="none" stroke="#fff" stroke-width="1.6"/></svg></p>
  </div>
</section>

<section>
  <h2 class="abs portfolio-title">OUR <b>PORTFOLIO</b></h2>

  <div class="abs project" style="left:77px;top:1702px"><div class="photo" role="img" aria-label="Renovated two-storey house in Rockaway" style="background:linear-gradient(180deg,#b7bcc0,#cdbfa2 50%,#557a35)"></div><h4>Rockaway, NJ</h4><p>Many upgrades to this home,<br>Added a new full bath, family...</p></div>
  <div class="abs project" style="left:348px;top:1702px"><div class="photo" role="img" aria-label="Teardown site with a small house in Denville" style="background:linear-gradient(180deg,#9b8f86,#8a8c93 50%,#6f6c6a)"></div><h4>Denville, NJ</h4><p>House was torn down. Using<br>portions of the foundation and...</p></div>
  <div class="abs project" style="left:618px;top:1702px"><div class="photo" role="img" aria-label="Small blue bungalow in Boonton" style="background:linear-gradient(180deg,#5f7d45,#7ba6b8 50%,#5f8f3a)"></div><h4>Boonton, NJ</h4><p>A complete remodel and add on<br>to this 2 bedroom house...</p></div>
  <div class="abs project" style="left:888px;top:1702px"><div class="photo" role="img" aria-label="Beige house on a stone-walled lot in Rockaway" style="background:linear-gradient(180deg,#d9dcdf,#cbbfa8 55%,#8c8578)"></div><h4>Rockaway, NJ</h4><p>Many upgrades to this home,<br>Added a new full bath, family...</p></div>

  <div class="abs project" style="left:77px;top:1995px"><div class="photo" role="img" aria-label="Renovated two-storey house in Rockaway" style="background:linear-gradient(180deg,#b7bcc0,#cdbfa2 50%,#557a35)"></div><h4>Rockaway, NJ</h4><p>Many upgrades to this home,<br>Added a new full bath, family...</p></div>
  <div class="abs project" style="left:348px;top:1995px"><div class="photo" role="img" aria-label="Teardown site with a small house in Denville" style="background:linear-gradient(180deg,#9b8f86,#8a8c93 50%,#6f6c6a)"></div><h4>Denville, NJ</h4><p>House was torn down. Using<br>portions of the foundation and...</p></div>
  <div class="abs project" style="left:618px;top:1995px"><div class="photo" role="img" aria-label="Small blue bungalow in Boonton" style="background:linear-gradient(180deg,#5f7d45,#7ba6b8 50%,#5f8f3a)"></div><h4>Boonton, NJ</h4><p>A complete remodel and add on<br>to this 2 bedroom house...</p></div>
  <div class="abs project" style="left:888px;top:1995px"><div class="photo" role="img" aria-label="Beige house on a stone-walled lot in Rockaway" style="background:linear-gradient(180deg,#d9dcdf,#cbbfa8 55%,#8c8578)"></div><h4>Rockaway, NJ</h4></div>
</section>

<footer>
  <div class="abs footer"></div>
  <svg class="abs footer-wave" viewBox="0 0 1200 60" preserveAspectRatio="none">
    <path d="M0 10 C250 40 500 48 720 40 C900 33 1050 20 1200 25 V60 H0 Z" fill="#545456"/>
    <path d="M0 10 C250 40 500 48 720 40 C900 33 1050 20 1200 25" fill="none" stroke="#2fa0d8" stroke-width="7"/>
  </svg>
  <div class="abs footer-brand"><div class="dot"></div><div class="name">PINECREST<br>HOLDINGS GROUP</div></div>
  <div class="abs fcol" style="left:350px">
    <h5>USEFUL LINKS</h5>
    <ul class="links"><li class="current">Home</li><li>About</li><li>Portfolio</li><li>Services</li></ul>
  </div>
  <div class="abs fcol" style="left:607px;width:260px">
    <h5>KEEP IN TOUCH</h5>
    <ul class="contact">
      <li><svg width="14" height="18" viewBox="0 0 14 18"><path d="M7 0a7 7 0 0 0-7 7c0 5 7 11 7 11s7-6 7-11a7 7 0 0 0-7-7zm0 10a3 3 0 1 1 0-6 3 3 0 0 1 0 6z" fill="#fff"/></svg><span>Morris County, NJ |<br>862-555-0148</span></li>
      <li><svg width="16" height="16" viewBox="0 0 24 24"><path fill="#fff" d="M6.6 10.8a15 15 0 0 0 6.6 6.6l2.2-2.2c.3-.3.7-.4 1-.2 1.1.4 2.3.6 3.6.6.6 0 1 .4 1 1V20c0 .6-.4 1-1 1A17 17 0 0 1 3 4c0-.6.4-1 1-1h3.5c.6 0 1 .4 1 1 0 1.3.2 2.5.6 3.6.1.3 0 .7-.2 1z"/></svg><span>123 456 7890</span></li>
      <li><svg width="17" height="13" viewBox="0 0 20 15"><rect x="1" y="1" width="18" height="13" fill="none" stroke="#fff" stroke-width="1.8"/><path d="M1 1 L10 8 L19 1" fill="none" stroke="#fff" stroke-width="1.8"/></svg><span>Info@pinecrestholdingsgroup.com</span></li>
    </ul>
  </div>
  <div class="abs fcol news" style="left:890px">
    <h5>NEWSLETTER</h5>
    <p>Subscribe to stay on Pinecrest Holdings Group</p>
    <div class="field">Enter Email id</div>
    <div class="subscribe">SUBSCRIBE</div>
  </div>
  <div class="abs bottombar">©&nbsp;<b>Pinecrest Holdings Group</b>&nbsp;- 2016. All Rights Reserved.</div>
</footer>

</body>
</html>
```